Brett Olsen Building Business Card Design

Hi,

I need a business card for my Building company.
I am a Builder and build homes for clients.
I am looking for a sophisticated logo that can be used on business cards, envelopes and letter heads.
I am trying to take my business to the next level and need a professional business card.

Colours: Please use white, black, dark grey and bright blue.

Thank you,

Carol and Brett.

Target Market(s)

1. Home and Building Companies 2. Potential customers

Industry/Entity Type

Business

Contact Information for Business Card

Brett Olsen Building PTY LTD

Brett Olsen

Director

A.B.N. 37 829 516 073

BUILDERS LICENCE No. 573019k

Mobile: 0412 907 381

Email: brettolsenbuilding@mailvane.com.au

Requirements
Must have
• The following is compulsory to have in the designs:

Brett Olsen Building PTY LTD (business name)

Brett Olsen (contact name)

Director (position)

A.B.N. 37 829 516 073

Builders Licence No. 573019k

Mobile: 0412 907 381

Nice to have
• Logo for business
Should not have
• Should not be cluttered.

I am looking for a clean, sophisticated and professional business card design.

```html
<!DOCTYPE html>
<html lang="en">
<head>
<meta charset="utf-8">
<title>Brett Olsen Building – Business Card</title>
<link rel="stylesheet" href="https://fonts.googleapis.com/css2?family=Roboto+Condensed:wght@400;700&family=Roboto:wght@400;700&display=swap">
<style>
  :root {
    --bg: #e9e7e3;
    --blue: #0f80c4;
    --blue-deep: #0a6aa9;
    --blue-light: #2ea6e2;
    --blue-text: #1d7cc0;
    --white: #ffffff;
    --mist: #e4e8ec;
    --paper: #f4f5f7;
    --paper-shade: #e6e8eb;
    --grey-dark: #55585c;
    --grey-mid: #7b7f84;
    --grey-line: #9aa0a6;
    --shadow: rgba(0, 0, 0, 0.18);
  }
  * { margin: 0; padding: 0; box-sizing: border-box; }
  html, body {
    width: 1200px;
    height: 880px;
    overflow: hidden;
    background: var(--bg);
  }
  .sheet {
    position: relative;
    width: 1200px;
    height: 880px;
  }
  .card {
    position: absolute;
    left: 290px;
    width: 620px;
    height: 354px;
    overflow: hidden;
    box-shadow: 0 6px 18px var(--shadow);
  }

  /* Front card */
  .card--front {
    top: 50px;
    background: linear-gradient(135deg, var(--blue) 0%, var(--blue-deep) 100%);
    font-family: "Roboto Condensed", Arial, sans-serif;
  }
  .card__waves { position: absolute; inset: 0; width: 100%; height: 100%; }
  .front-brand {
    position: absolute;
    left: 0;
    right: 0;
    top: 120px;
    text-align: center;
    color: var(--mist);
    font-weight: 700;
  }
  .front-brand__name { font-size: 46px; letter-spacing: 0.2px; }
  .front-brand__suffix { font-size: 16px; margin-left: 8px; }
  .front-credentials {
    position: absolute;
    left: 34px;
    right: 34px;
    bottom: 26px;
    color: var(--white);
    font-size: 19px;
    display: flex;
    gap: 12px;
    align-items: center;
  }
  .front-credentials strong { font-weight: 700; }
  .front-credentials .dot {
    width: 7px; height: 7px; border-radius: 50%; background: var(--white);
    display: inline-block;
  }

  /* Back card */
  .card--back {
    top: 464px;
    background: linear-gradient(160deg, var(--white) 0%, var(--paper) 60%, var(--paper-shade) 100%);
    font-family: "Roboto", Arial, sans-serif;
  }
  .back-brand {
    position: absolute;
    left: 60px;
    top: 78px;
    color: var(--grey-dark);
    font-family: "Roboto Condensed", Arial, sans-serif;
    font-weight: 700;
  }
  .back-brand__name { font-size: 30px; }
  .back-brand__suffix { font-size: 11px; margin-left: 5px; }
  .back-divider {
    position: absolute;
    left: 236px;
    top: 160px;
    width: 1px;
    height: 108px;
    background: var(--grey-line);
  }
  .contact {
    position: absolute;
    left: 256px;
    top: 168px;
    color: var(--grey-dark);
  }
  .contact__name { color: var(--blue-text); font-size: 23px; font-weight: 700; }
  .contact__role { color: var(--grey-mid); font-size: 16px; margin-top: 2px; }
  .contact__lines { margin-top: 22px; font-size: 16px; line-height: 1.45; }
  .contact__lines strong { font-weight: 700; }
</style>
</head>
<body>
<main class="sheet">

  <section class="card card--front" aria-label="Business card front">
    <svg class="card__waves" viewBox="0 0 620 354" preserveAspectRatio="none" aria-hidden="true">
      <path d="M0 262 C 180 222, 420 228, 620 290 L620 354 L0 354 Z" fill="#2a9ad8" opacity="0.55"/>
      <path d="M0 286 C 200 248, 420 256, 620 312 L620 354 L0 354 Z" fill="#36aae6" opacity="0.6"/>
      <path d="M0 262 C 180 222, 420 228, 620 290" fill="none" stroke="#5cc0f0" stroke-width="1.5" opacity="0.6"/>
    </svg>
    <h1 class="front-brand">
      <span class="front-brand__name">Brett Olsen Building</span><span class="front-brand__suffix">PTY LTD</span>
    </h1>
    <p class="front-credentials">
      <span><strong>A.B.N.</strong> 37 829 516 073</span>
      <span class="dot"></span>
      <span><strong>Builders Licence No.</strong> 573019k</span>
    </p>
  </section>

  <section class="card card--back" aria-label="Business card back">
    <svg class="card__waves" viewBox="0 0 620 354" preserveAspectRatio="none" aria-hidden="true">
      <path d="M0 190 C 120 200, 200 250, 250 354 L0 354 Z" fill="#e3e6e9"/>
      <path d="M0 222 C 200 220, 420 300, 620 330 L620 354 L0 354 Z" fill="#dfe2e6" opacity="0.7"/>
      <path d="M0 250 C 220 250, 420 320, 620 340" fill="none" stroke="#d2d6da" stroke-width="2"/>
    </svg>
    <h2 class="back-brand">
      <span class="back-brand__name">Brett Olsen Building</span><span class="back-brand__suffix">PTY LTD</span>
    </h2>
    <div class="back-divider"></div>
    <div class="contact">
      <p class="contact__name">Brett Olsen</p>
      <p class="contact__role">Director</p>
      <p class="contact__lines">
        <strong>Mobile:</strong> 0412 907 381<br>
        <strong>Email:</strong> brettolsenbuilding@mailvane.com.au
      </p>
    </div>
  </section>

</main>
</body>
</html>
```